Health care technology software systems

We have a solid logo. We have company colors that will need to be used as well. We just need a great business card design. We sell to health plans but want to be modern
Updates

Need extra days to review

Target Market(s)

Health technology sector selling into Health Plans

Industry/Entity Type

Health Care Technology

Contact Information for Business Card

Name, title, address, phone number, email

Requirements
Must have
• Use of Kembrata corporate colors - Uploaded w/ our logos

```html
<!DOCTYPE html>
<html lang="en">
<head>
<meta charset="utf-8">
<title>Kembrata Business Card</title>
<link rel="stylesheet" href="https://fonts.googleapis.com/css2?family=Montserrat:wght@300;400&family=Roboto:wght@400&display=swap">
<style>
  :root {
    --stage: #e3e5e4;
    --card: #363030;
    --green: #7dc242;
    --band-green: #4f5a35;
    --band-teal: #2e4f5c;
    --band-navy: #363a50;
    --white: #ffffff;
    --grey: #8a8585;
    --card-shadow: 0 6px 14px rgba(0,0,0,0.18);
  }
  * { box-sizing: border-box; margin: 0; padding: 0; }
  html, body { width: 1200px; height: 800px; overflow: hidden; }
  body {
    background: var(--stage);
    display: flex;
    align-items: center;
    justify-content: center;
    gap: 40px;
  }
  .card {
    position: relative;
    width: 540px;
    height: 300px;
    background: var(--card);
    overflow: hidden;
    box-shadow: var(--card-shadow);
  }
  .band {
    position: absolute;
    top: 0;
    height: 100%;
  }
  .card--front .band--green { left: 0; width: 22px; background: var(--band-green); }
  .card--front .band--teal { left: 22px; width: 32px; background: var(--band-teal); }
  .card--back .band--navy { right: 70px; width: 36px; background: var(--band-navy); }
  .card--back .band--green { right: 0; width: 70px; background: var(--band-green); }
  .brand {
    position: absolute;
    display: flex;
    align-items: center;
    gap: 10px;
    font-family: "Montserrat", sans-serif;
    font-weight: 300;
    color: var(--white);
    letter-spacing: 1px;
    white-space: nowrap;
  }
  .brand__dot {
    width: 14px;
    height: 14px;
    border-radius: 50%;
    background: var(--green);
  }
  .card--front .brand { left: 72px; top: 126px; font-size: 31px; }
  .divider {
    position: absolute;
    left: 284px;
    top: 118px;
    width: 2px;
    height: 70px;
    background: var(--green);
  }
  .person {
    position: absolute;
    left: 302px;
    top: 62px;
    font-family: "Montserrat", sans-serif;
  }
  .person__name { font-size: 20px; font-weight: 400; color: var(--green); letter-spacing: 0.5px; white-space: nowrap; }
  .person__title { font-size: 15px; font-weight: 400; color: var(--grey); margin-top: 2px; letter-spacing: 0.5px; }
  .contact {
    position: absolute;
    left: 302px;
    top: 128px;
    font-family: "Roboto", sans-serif;
    font-size: 15px;
    line-height: 24px;
    color: var(--white);
  }
  .address {
    position: absolute;
    left: 302px;
    top: 214px;
    font-family: "Roboto", sans-serif;
    font-size: 15px;
    line-height: 22px;
    color: var(--grey);
    font-style: normal;
  }
  .card--back .brand { right: 130px; bottom: 48px; font-size: 44px; }
</style>
</head>
<body>
  <section class="card card--front" aria-label="Business card front">
    <div class="band band--green"></div>
    <div class="band band--teal"></div>
    <div class="brand"><span class="brand__dot"></span>kembrata</div>
    <div class="divider"></div>
    <div class="person">
      <p class="person__name">Daniel Hargrove</p>
      <p class="person__title">President</p>
    </div>
    <div class="contact">
      <p>555-214-3870</p>
      <p>hello@kembrata.com</p>
    </div>
    <address class="address">
      48 Linden Ave,<br>Suite 100, City, NY 10458
    </address>
  </section>

  <section class="card card--back" aria-label="Business card back">
    <div class="band band--navy"></div>
    <div class="band band--green"></div>
    <div class="brand">kembrata</div>
  </section>
</body>
</html>
```